Poster promoting the "Golden Sheaf Day"

The Allied Guild of Millers and Pastrymakers (AGMP) created the "Golden Sheaf Day" in 2006. It is celebreated each year together with the ORV "Common Table Day" on 16th October.
After using different posters for a few years, AGMP decided to settle on a permanent poster some time ago, in order to allow people to recognize the poster long-term.
Now, AGMP feels that this permanent poster needs an update and modernization, apart from including the new AGMP logo.
Requisits:
1. Must include the new AGMP logo
2. The poster should reflect the importance of bread in the world and convey an image of health, innovation and tradition.
3. One version with text, one version without text
4. Text version: one poster for each of the four official AGMP languages:
ENGLISH: Golden Sheaf Day / 16th October
GERMAN: Tag der Goldenen Garbe / 16. Oktober
SPANISH: Día de la Gavilla Dorada / 16 de Octubre
FRENCH: Journée de la Gerbe Dorée / 16 Octobre
5. Colours must be defined with RGB colour code.
AGMP will take a decision regarding the new poster design during the next meeting of its Marketing Commission on March 24th, 2015. Therefore, please submit your proposals by 18th March in order to allow for pre-selection and modification requests.
More about AGMP at www.alliedguildmp.org.

```html
<!DOCTYPE html>
<html lang="en">
<head>
<meta charset="utf-8">
<title>Golden Sheaf Day Poster</title>
<link rel="stylesheet" href="https://fonts.googleapis.com/css2?family=Montserrat:wght@500;700;800&display=swap">
<style>
  :root {
    --page-bg: #dfe5ea;
    --wood-dark: #2a1c16;
    --wood-mid: #4a3327;
    --crust-gold: #c98a45;
    --crust-light: #e9c48e;
    --accent-orange: #f0902f;
    --text-white: #ffffff;
    --text-muted: #cfc3b8;
    --rule-gold: #c9a77c;
  }
  * { margin: 0; padding: 0; box-sizing: border-box; }
  html, body {
    width: 1200px;
    height: 960px;
    overflow: hidden;
    background: var(--page-bg);
    font-family: "Montserrat", sans-serif;
  }
  .poster {
    position: absolute;
    left: 279px;
    top: 30px;
    width: 642px;
    height: 900px;
    overflow: hidden;
    background: var(--wood-dark);
  }
  .poster__photo {
    position: absolute;
    inset: 0;
    background:
      radial-gradient(ellipse 46% 32% at 62% 28%, var(--crust-light) 0%, var(--crust-gold) 45%, rgba(74,51,39,0) 100%),
      radial-gradient(ellipse 22% 14% at 58% 64%, #a9773f 0%, rgba(74,51,39,0) 100%),
      radial-gradient(ellipse 40% 10% at 78% 5%, #e3b77a 0%, rgba(74,51,39,0) 100%),
      linear-gradient(180deg, var(--wood-mid) 0%, var(--wood-dark) 100%);
  }
  .brand {
    position: absolute;
    left: 42px;
    top: 34px;
    display: flex;
    align-items: center;
    gap: 10px;
  }
  .brand__mark {
    width: 14px;
    height: 14px;
    border-radius: 50%;
    background: var(--accent-orange);
  }
  .brand__name {
    font-weight: 700;
    font-size: 26px;
    color: var(--accent-orange);
    letter-spacing: 1px;
  }
  .headline {
    position: absolute;
    left: 0;
    width: 100%;
    text-align: center;
  }
  .headline__lead {
    top: 606px;
    font-weight: 700;
    font-size: 46px;
    color: var(--text-white);
    letter-spacing: -0.5px;
  }
  .headline__main {
    top: 640px;
    font-weight: 800;
    font-size: 150px;
    line-height: 1;
    color: var(--accent-orange);
    letter-spacing: -3px;
  }
  .date-line {
    position: absolute;
    left: 0;
    top: 790px;
    width: 100%;
    display: flex;
    justify-content: center;
    align-items: center;
    gap: 18px;
  }
  .date-line__rule {
    width: 90px;
    height: 2px;
    background: var(--rule-gold);
  }
  .date-line__text {
    font-weight: 700;
    font-size: 30px;
    color: var(--text-white);
  }
  .website {
    position: absolute;
    left: 0;
    top: 838px;
    width: 100%;
    text-align: center;
    font-weight: 500;
    font-size: 17px;
    color: var(--text-muted);
    letter-spacing: 0.3px;
  }
</style>
</head>
<body>
  <main class="poster">
    <div class="poster__photo" role="img" aria-label="Photograph of baguettes, a round scored country loaf, a sesame roll and wheat ears on a dark wooden table"></div>

    <div class="brand">
      <span class="brand__mark"></span>
      <span class="brand__name">AGMP</span>
    </div>

    <h1>
      <span class="headline headline__lead">GOLDEN SHEAF</span>
      <span class="headline headline__main">DAY</span>
    </h1>

    <div class="date-line">
      <span class="date-line__rule"></span>
      <span class="date-line__text">16TH OCTOBER</span>
      <span class="date-line__rule"></span>
    </div>

    <p class="website">alliedguildmp.org</p>
  </main>
</body>
</html>
```